Ferrowave.com website design

I need a basic website for www.ferrowave.com. Ferro Wave has been hosting websites since 2002 via partnership arrangement with Stackhollow.com and Namequarry.com. We do not do any design, only hosting for small companies and nonprofits. We are referring people to PixelGuild and others to get their websites developed. Our website and pricing does not change often, but I need to be able to easily update the pricing and contact page.

Target Market(s)

Small company and non profit organizations

Industry/Entity Type

Utility

Coding

Coded - Design and coding required

Number of Pages Required

5+ page

Colors

Designer to choose colors to be used in the design.

Requirements
Must have
• Wordsmith format for easy content management. The logo attached. Contact us page with the following: Phone and fax are the same number: 888.514.2973. Email address is myferrowave@mailnest.example. Mailing address is 4819 E. Tolliver Bend #317, Halden Ridge, MO 64831.
Nice to have
• Some kind of badge or tag line on the home page that celebrates our 15th year of hosting without a single hosting without any downtime. We are are 15 year partners with Stackhollow.com and Namequarry.com. Website Design tab needs to reference PixelGuild or others for all their website design needs. We provide no design or updating services. We will provide the developers FTP access to our dedicated Linux server. We do not provide email services other than redirects to their proprietary email or gmail, yahoo, etc. Needs a services and pricing tab. We provide domain registration services via our partnership with Namequarry.com. We will want a way for them to submit a suggested domain name for us to verify if available. I might be able to get a link from Namequarry.com to our account for you to include on that tab REGISTER DOMAIN. The tab buttons can be: WHO WE ARE, WHAT WE DO, WHEN YOU NEED US, WHERE TO REACH US. Maybe consider making the WHO, WHAT, WHEN and WHERE a dark blue color the rest of the text different color just so they stand out
Should not have
• A lot of animation that takes a long time to open. Clean and simple website.

```html
<!DOCTYPE html>
<html lang="en">
<head>
<meta charset="utf-8">
<title>Ferro Wave – Website Hosting</title>
<link rel="stylesheet" href="https://fonts.googleapis.com/css2?family=Baloo+2:wght@600;700&family=Roboto:wght@400;500;700&family=Lora:ital@1&display=swap">
<style>
:root{
  --navy:#0d4a80;
  --blue:#2f86c8;
  --blue-mid:#1c6aa8;
  --sky:#dbe9f3;
  --green:#7cc242;
  --ink:#222;
  --text:#555;
  --yellow:#f6eea0;
  --footer:#0c4f88;
  --white:#fff;
  --gold:#d9a624;
}
*{box-sizing:border-box;margin:0;padding:0}
html,body{width:1200px;height:2381px;overflow:hidden;background:var(--white)}
body{font-family:"Roboto",sans-serif;color:var(--text);position:relative}
.page{position:relative;width:1200px;height:2381px;overflow:hidden}
.abs{position:absolute}

/* header */
.site-header{left:0;top:0;width:1200px;height:111px;background:var(--white);border-bottom:1px solid #ddd}
.brand{left:71px;top:30px;display:flex;align-items:center;gap:12px}
.brand-mark{width:40px;height:40px;background:var(--blue-mid)}
.brand-name{font-family:"Roboto",sans-serif;font-weight:700;font-size:26px;color:var(--navy);letter-spacing:.5px}
.main-nav{left:330px;top:46px;display:flex;gap:24px;font-size:13.5px;font-weight:700;color:var(--navy)}
.sign-up{left:833px;top:46px;font-size:13.5px;font-weight:500;color:var(--navy);display:flex;align-items:center;gap:8px}
.quote-btn{left:943px;top:36px;width:184px;height:39px;border:2px solid var(--green);color:var(--green);font-size:13.5px;font-weight:500;display:flex;align-items:center;justify-content:center}

/* hero */
.hero{left:0;top:111px;width:1200px;height:552px;background:linear-gradient(110deg,#0d3f70 0%,#1f5f98 45%,#3876b0 70%,#15497c 100%)}
.hero-mark{left:576px;top:258px;width:48px;height:48px;border:4px solid var(--white)}
.hero-title{left:0;top:322px;width:1200px;text-align:center;font-family:"Baloo 2",sans-serif;font-weight:700;font-size:38px;color:var(--white)}
.search{left:336px;top:414px;width:526px;height:52px;background:var(--white);border-radius:26px;border:3px solid #cfe0ef}
.search-placeholder{left:28px;top:14px;font-size:14px;color:#888}
.search-btn{right:0;top:0;width:168px;height:46px;border-radius:23px;background:var(--blue);color:var(--white);font-size:14px;font-weight:500;display:flex;align-items:center;justify-content:center}
.hero-note{left:0;top:488px;width:1200px;text-align:center;font-size:14px;line-height:21px;color:var(--white)}

/* badge band */
.badge-band{left:0;top:663px;width:1200px;height:115px;background:var(--sky)}
.badge{left:208px;top:613px;width:134px;height:134px;border-radius:50%;background:var(--gold);border:10px solid #f3d36a}
.badge-text{left:397px;top:695px;font-size:16px;font-weight:500;line-height:25px;color:#333}
.badge-text em{font-weight:700;color:var(--navy)}

/* welcome */
.welcome{left:73px;top:832px;width:390px}
.welcome h2{font-weight:400;font-size:27px;color:var(--ink);margin-bottom:18px}
.welcome h2 span{color:var(--blue)}
.welcome p{font-size:13.5px;line-height:22px;color:var(--text);margin-bottom:22px}
.col-divider{left:495px;top:778px;width:1px;height:460px;background:#e6e6e6}
.btn-outline{height:38px;border:1.5px solid var(--blue);color:var(--blue-mid);font-size:13px;font-weight:500;display:flex;align-items:center;justify-content:center;border-radius:2px}
.feature{top:833px;width:286px;text-align:center}
.feature-img{width:286px;height:187px;border-radius:2px}
.feature h3{font-size:16px;font-weight:500;color:var(--ink);margin:22px 0 10px}
.feature p{font-size:13.5px;line-height:22px;color:var(--text);padding:0 10px}
.feature .btn-outline{width:110px;margin:18px auto 0}

/* solution band */
.solution-band{left:0;top:1240px;width:1200px;height:126px;background:var(--navy)}
.solution-title{left:184px;top:1285px;font-family:"Baloo 2",sans-serif;font-weight:600;font-size:28px;color:var(--white)}
.solution-mark{left:112px;top:1283px;width:44px;height:44px;border:4px solid var(--white)}
.solution-phone{left:882px;top:1293px;font-size:27px;font-weight:700;color:var(--white);display:flex;align-items:center;gap:12px}

/* why */
.why-title{left:73px;top:1415px;width:692px;text-align:center;font-size:23px;font-weight:400;color:var(--ink)}
.why-title::before{content:"";position:absolute;left:0;right:0;top:16px;height:4px;background:#eee;z-index:0}
.why-title span{position:relative;background:var(--white);padding:0 12px}
.perk{top:1476px;width:210px;text-align:center}
.perk svg{display:block;margin:0 auto}
.perk h4{font-size:15.5px;font-weight:500;color:var(--ink);margin:22px 0 12px}
.perk p{font-size:13.5px;line-height:22px;color:var(--text);padding:0 4px}
.partners{left:794px;top:1368px;width:333px;height:346px;background:var(--yellow);text-align:center}
.partners p{margin:52px 40px 0;font-size:15px;font-weight:500;line-height:23px;color:#444}
.partner-name{font-size:32px;font-weight:700;display:block}
.partner-one{margin-top:44px;color:#222}
.partner-two{margin-top:30px;color:#3a8a3a}

/* testimonial */
.testimonials{left:0;top:1714px;width:1200px;height:360px;background:linear-gradient(180deg,#b9cbdc,#d6e2ec 50%,#b7c9db)}
.quote-card{left:165px;top:1771px;width:871px;height:264px;background:var(--white);text-align:center}
.quote-card p{margin:70px 64px 0;font-family:"Lora",serif;font-style:italic;font-size:16px;line-height:26px;color:#444}
.quote-card cite{display:block;margin-top:18px;font-family:"Roboto",sans-serif;font-style:normal;font-size:15px;font-weight:500;color:var(--blue)}
.arrow{top:1880px;width:46px;height:46px;border-radius:50%;background:var(--white);border:2px solid #223}

/* footer */
.site-footer{left:0;top:2074px;width:1200px;height:267px;background:var(--footer)}
.footer-deco{left:72px;top:2110px;width:200px;height:200px;background:#14599a}
.footer-col{top:2104px;color:#c9d9ea;font-size:13.5px;line-height:21px}
.footer-col h5{font-size:15.5px;font-weight:500;color:var(--white);margin-bottom:18px}
.news-date{display:inline-block;background:#2d76b8;color:var(--white);font-size:12.5px;padding:0 4px;border:1px solid #8fb7db}
.news-item{margin-bottom:12px}
.email-input{width:245px;height:42px;background:var(--white);border-radius:3px;color:#888;font-size:13.5px;padding:12px 14px}
.subscribe-btn{width:245px;height:42px;margin-top:8px;background:var(--blue);border-radius:3px;color:var(--white);font-weight:500;font-size:14px;display:flex;align-items:center;justify-content:center}
.social{display:flex;gap:10px;margin:14px 0 0 82px}
.social span{width:34px;height:34px;background:#8ea6bd}
.copyright{left:0;top:2341px;width:1200px;height:40px;background:var(--sky);text-align:center;font-size:13.5px;line-height:40px;color:#666}
</style>
</head>
<body>
<div class="page">

<header class="site-header abs">
  <div class="brand abs"><span class="brand-mark"></span><span class="brand-name">FERRO WAVE</span></div>
  <nav class="main-nav abs"><span>HOME</span><span>PRICING</span><span>WHO</span><span>WHAT</span><span>WHEN</span><span>WHERE</span><span>CONTACT</span></nav>
  <div class="sign-up abs"><svg width="14" height="14" viewBox="0 0 14 14"><circle cx="7" cy="4" r="3.2" fill="#2f86c8"/><path d="M1 14c0-4 3-6 6-6s6 2 6 6z" fill="#2f86c8"/></svg>SIGN UP</div>
  <div class="quote-btn abs">REQUEST FREE QUOTE</div>
</header>

<section class="hero abs" role="img" aria-label="Photo of a smiling woman working at a laptop, tinted blue"></section>
<div class="hero-mark abs"></div>
<h1 class="hero-title abs">Finding A Great Domain Name is Easy</h1>
<div class="search abs">
  <span class="search-placeholder abs">Find the domain that's right for you...</span>
  <span class="search-btn abs">SEARCH DOMAIN</span>
</div>
<p class="hero-note abs">Ferro Wave has been hosting websites since 2002 via<br>partnership arrangement with Stackhollow.com and Namequarry.com.</p>

<section class="badge-band abs"></section>
<div class="badge abs" role="img" aria-label="Celebrating 15 years badge"></div>
<p class="badge-text abs">Celebrates our 15th year of hosting without a single hosting without any downtime.<br>We are are 15 year partners with <em>Stackhollow.com</em> and <em>Namequarry.com</em></p>

<section class="welcome abs">
  <h2>Welcome to <span>Ferrowave</span></h2>
  <p>Lorem Ipsum is simply dummy text of the printing and typesetting industry. Lorem Ipsum has been the industry's standard dummy text ever since the 1500s, when an unknown printer took a galley of type and scrambled it to make a type specimen book.</p>
  <p>It has survived not only five centuries, but also the leap into electronic typesetting, remaining essentially unchanged. It was popularised in the 1960s with the release of Letraset sheets containing Lorem Ipsum passages, and more recently with versions of Lorem Ipsum.</p>
  <div class="btn-outline" style="width:110px">READ MORE</div>
</section>
<div class="col-divider abs"></div>

<article class="feature abs" style="left:524px">
  <div class="feature-img" role="img" aria-label="Photo of hands arranging website wireframe sketches" style="background:linear-gradient(135deg,#c9cfcc,#8e9a97 60%,#5e6b6a)"></div>
  <h3>Web Content Management</h3>
  <p>Lorem Ipsum is simply dummy text of the Ipsum has been the industry's standard dummy text ever since</p>
  <div class="btn-outline">READ MORE</div>
</article>
<article class="feature abs" style="left:840px">
  <div class="feature-img" role="img" aria-label="Photo of a rack of servers with blue light" style="background:linear-gradient(135deg,#0e2f66,#2a6fc0 55%,#0b2250)"></div>
  <h3>Dedicated Linux server</h3>
  <p>Lorem Ipsum is simply dummy text of the Ipsum has been the industry's standard dummy text ever since</p>
  <div class="btn-outline">READ MORE</div>
</article>

<section class="solution-band abs">
  <svg class="abs" style="left:0;top:0" width="1200" height="126" viewBox="0 0 1200 126">
    <polygon points="0,14 690,14 817,114 0,114" fill="#3a8fd0"/>
    <polygon points="0,0 700,0 712,10 0,10" fill="#2a78bd"/>
    <polygon points="455,118 820,118 826,126 460,126" fill="#2a78bd"/>
  </svg>
</section>
<div class="solution-mark abs"></div>
<h2 class="solution-title abs">Find The Right Solution For Your Business</h2>
<div class="solution-phone abs"><svg width="18" height="30" viewBox="0 0 18 30"><rect x="1.5" y="1.5" width="15" height="27" rx="3" fill="none" stroke="#fff" stroke-width="2.5"/><circle cx="9" cy="24" r="1.6" fill="#fff"/></svg>888.514.2973</div>

<h2 class="why-title abs"><span>Why Choose Us?</span></h2>
<div class="perk abs" style="left:78px">
  <svg width="70" height="72" viewBox="0 0 70 72"><circle cx="35" cy="18" r="12" fill="#7cc242"/><path d="M20 18a15 15 0 0 1 30 0" fill="none" stroke="#7cc242" stroke-width="4"/><rect x="12" y="40" width="46" height="24" rx="3" fill="#7cc242"/><rect x="4" y="64" width="62" height="6" rx="2" fill="#7cc242"/></svg>
  <h4>24/7 Customer Support</h4>
  <p>Lorem Ipsum is simply dummy text of the Ipsum has been the ever since</p>
</div>
<div class="perk abs" style="left:315px">
  <svg width="70" height="72" viewBox="0 0 70 72"><circle cx="35" cy="40" r="27" fill="none" stroke="#7cc242" stroke-width="5"/><rect x="29" y="2" width="12" height="7" fill="#7cc242"/><path d="M35 24v17h12" fill="none" stroke="#7cc242" stroke-width="5"/></svg>
  <h4>Fast and Reliable</h4>
  <p>Lorem Ipsum is simply dummy text of the Ipsum has been the ever since</p>
</div>
<div class="perk abs" style="left:552px">
  <svg width="70" height="72" viewBox="0 0 70 72"><rect x="4" y="8" width="62" height="60" rx="3" fill="none" stroke="#7cc242" stroke-width="4"/><path d="M4 22h62M18 2v12M52 2v12M16 32h38v28H16zM29 32v28M41 32v28M16 46h38" fill="none" stroke="#7cc242" stroke-width="3"/></svg>
  <h4>Improve Everyday</h4>
  <p>Lorem Ipsum is simply dummy text of the Ipsum has been the ever since</p>
</div>
<aside class="partners abs">
  <p>Over 3 million small businesses rely on Stackhollow.com and Namequarry.com every day.</p>
  <span class="partner-name partner-one">stackhollow</span>
  <span class="partner-name partner-two">namequarry.com</span>
</aside>

<section class="testimonials abs" role="img" aria-label="Faded grid of customer portrait photos"></section>
<blockquote class="quote-card abs">
  <svg class="abs" style="left:420px;top:32px" width="30" height="24" viewBox="0 0 30 24"><path d="M0 24V12C0 5 4 1 11 0v5c-3 1-5 3-5 7h5v12zM17 24V12c0-7 4-11 11-12v5c-3 1-5 3-5 7h5v12z" fill="#2f86c8"/></svg>
  <p>“It has survived not only five centuries, but also the leap into electronic typesetting, remaining essentially unchanged. It was popularised in the 1960s with the release of Letraset sheets containing Lorem Ipsum passages, and it was popularised in the 1960s with the release of Letraset sheets more recently with versions of Lorem Ipsum.”<cite>- Marcus Hale</cite></p>
</blockquote>
<div class="arrow abs" style="left:142px"><svg width="42" height="42" viewBox="0 0 42 42"><path d="M24 14l-7 7 7 7" fill="none" stroke="#2f86c8" stroke-width="2.5"/></svg></div>
<div class="arrow abs" style="left:1012px"><svg width="42" height="42" viewBox="0 0 42 42"><path d="M18 14l7 7-7 7" fill="none" stroke="#2f86c8" stroke-width="2.5"/></svg></div>

<footer class="site-footer abs"></footer>
<div class="footer-deco abs"></div>
<div class="footer-col abs" style="left:343px;width:240px">
  <h5>Recent News</h5>
  <div class="news-item"><span class="news-date">25 MAR 2017</span><br>Lorem Ipsum is simply dummy text<br>has been the ever since.</div>
  <div class="news-item"><span class="news-date">30 MAR 2017</span><br>Lorem Ipsum is simply dummy text<br>has been the ever since.</div>
</div>
<div class="footer-col abs" style="left:632px;width:230px">
  <h5>Contact Information</h5>
  <p>Ferrowave<br>4819 E. Tolliver Bend #317,<br>Halden Ridge, MO 64831.</p>
  <p style="margin-top:12px">T: 888.514.2973<br>F: 888.514.2973<br>myferrowave@mailnest.example</p>
</div>
<div class="footer-col abs" style="left:882px;width:245px">
  <h5>Subscribe Newsletter!</h5>
  <div class="email-input">Email Address</div>
  <div class="subscribe-btn">SUBSCRIBE</div>
  <div class="social"><span></span><span></span></div>
</div>
<div class="copyright abs">Copyright 2017Ferrowave. All Rights Reserved</div>

</div>
</body>
</html>
```